New Business Cards for NYC Salon

We are updating all of our cards. 7142-2869-4057 is my account number. We put names of our stylists on their cards. The back should include appointment space. Were looking for something more sleek and modern. Black/White Silver... or even touches of the orange color on our website which has been our thing for years. The design should communicate professional upscale boutique salon for men and women. Should be able to incorporate design into thank you cards, referral cards, brochure and postcards. The file is a zip file...we like the stacked ones black or white or the side versions.

Industry/Entity Type

Beauty Salon

Contact Information for Business Card

Marcus John's Salon313 W. 53rd Street, New York NY 10019 212-386-7714 info@marcusdellsalon.example www.marcusdellsalon.example

Font styles to use
Other font styles liked:
• trajan

Requirements
Must have
• we print a different card for every person in the salon. Begin by designing with the name Marcus. We will change it with every employee when printing. Must have a space for appointment date and time.
Nice to have
• Were looking to move towards the stacked or side placed logo but not opposed to utilizing the circular.
Should not have
• Photos

```html
<!DOCTYPE html>
<html lang="en">
<head>
<meta charset="utf-8">
<title>Marcus Dell's Salon – Business Card</title>
<link href="https://fonts.googleapis.com/css2?family=Open+Sans:wght@400;600;700&display=swap" rel="stylesheet">
<style>
  :root {
    --backdrop: #3b3430;
    --card: #151515;
    --card-edge: #0b0b0b;
    --ink: #ffffff;
    --rule: #8a8a8a;
    --icon-ink: #151515;
  }
  * { box-sizing: border-box; margin: 0; padding: 0; }
  html, body { width: 1200px; height: 844px; overflow: hidden; }
  body {
    background: var(--backdrop);
    font-family: "Open Sans", Arial, sans-serif;
    color: var(--ink);
    position: relative;
  }
  .card {
    position: absolute;
    width: 530px;
    height: 303px;
    background: var(--card);
    border: 1px solid var(--card-edge);
    border-radius: 4px;
    box-shadow: 0 14px 30px rgba(0,0,0,.45);
  }
  .card--front { left: 45px; top: 270px; }
  .card--back { left: 625px; top: 270px; }

  /* front */
  .brand {
    position: absolute;
    left: 150px; top: 48px;
    display: flex; align-items: center; gap: 12px;
  }
  .brand__dot {
    width: 26px; height: 26px; border-radius: 50%;
    border: 2px solid var(--ink);
  }
  .brand__name {
    font-size: 15px; font-weight: 400; letter-spacing: 3px; text-transform: uppercase;
  }
  .holder {
    position: absolute; left: 36px; top: 176px;
    font-size: 21px; font-weight: 600;
  }
  .address {
    position: absolute; left: 36px; top: 232px;
    font-size: 15px; line-height: 22px;
  }
  .contacts {
    position: absolute; right: 28px; top: 138px;
    list-style: none; text-align: right;
    font-size: 14px; line-height: 22px;
  }
  .contacts li { display: flex; justify-content: flex-end; align-items: center; gap: 8px; }
  .contacts svg { width: 15px; height: 15px; flex: none; }

  /* back */
  .appt__title {
    position: absolute; left: 0; right: 0; top: 36px;
    text-align: center; font-size: 18px; font-weight: 700;
  }
  .appt__row {
    position: absolute; left: 44px; right: 44px;
    display: flex; align-items: flex-end; gap: 8px;
    font-size: 13px;
  }
  .appt__row--name { top: 92px; }
  .appt__row--date { top: 132px; }
  .appt__row--time { top: 172px; }
  .appt__label { width: 50px; flex: none; }
  .appt__line { flex: 1; border-bottom: 1px solid var(--rule); height: 14px; }
  .appt__note {
    position: absolute; left: 0; right: 0; top: 232px;
    text-align: center; font-size: 13px; font-weight: 600;
  }
</style>
</head>
<body>
  <section class="card card--front" aria-label="Business card front">
    <div class="brand">
      <span class="brand__dot"></span>
      <span class="brand__name">Marcus Dell's Salon</span>
    </div>
    <p class="holder">Marcus Dell's Salon</p>
    <p class="address">748 E. 29th Street,<br>New York NY 10016</p>
    <ul class="contacts">
      <li>212-386-7714
        <svg viewBox="0 0 16 16" aria-hidden="true"><rect width="16" height="16" rx="3" fill="#fff"/><path d="M4.5 3.5l2 .3.6 2.2-1.2.9a6 6 0 0 0 3.2 3.2l.9-1.2 2.2.6.3 2c-.4.6-1.2 1-2 .9C7 12 4 9 3.6 5.5c-.1-.8.3-1.6.9-2z" fill="var(--icon-ink)"/></svg>
      </li>
      <li>info@marcusdellsalon.example
        <svg viewBox="0 0 16 16" aria-hidden="true"><rect width="16" height="16" rx="3" fill="#fff"/><rect x="3.5" y="5" width="9" height="6.5" fill="var(--icon-ink)"/><path d="M3.8 5.3L8 8.6l4.2-3.3" stroke="#fff" stroke-width="1" fill="none"/></svg>
      </li>
      <li>marcusdellsalon.example
        <svg viewBox="0 0 16 16" aria-hidden="true"><rect width="16" height="16" rx="3" fill="#fff"/><path d="M6.8 9.2l2.4-2.4M7.5 5.2l1-1a2 2 0 0 1 2.8 2.8l-1 1M8.5 10.8l-1 1a2 2 0 0 1-2.8-2.8l1-1" stroke="var(--icon-ink)" stroke-width="1.4" fill="none" stroke-linecap="round"/></svg>
      </li>
    </ul>
  </section>

  <section class="card card--back" aria-label="Business card back, appointment reminder">
    <h2 class="appt__title">Your Next Appointment is</h2>
    <div class="appt__row appt__row--name"><span class="appt__label">Name :</span><span class="appt__line"></span></div>
    <div class="appt__row appt__row--date"><span class="appt__label">Date :</span><span class="appt__line"></span></div>
    <div class="appt__row appt__row--time"><span class="appt__label">Time:</span><span class="appt__line"></span><span>AM</span><span class="appt__line"></span><span>PM</span></div>
    <p class="appt__note">If unable to keep appointment, kindly give 24hrs notice.</p>
  </section>
</body>
</html>
```